SkyvoraQ Business Cards and Stationary Design

Need a design for our business cards and stationary. I want to carry on the theme of the logo. I want the business cards to have a design on the back. I would like the business cards and the stationary to carry the same theme, design scheme, and branding

Target Market(s)

Airlines and Maintenance Facilities

Industry/Entity Type

Aviation

Contact Information for Business Card

Name
Position Title
Address: 4827 Tollbeck Lane, Marrowick, FL 34951
Office Number
Mobile Number
Email
Website

Font styles to use
Serif
Sans Serif

Colors

Designer to choose colors to be used in the design.

```html
<!DOCTYPE html>
<html lang="en">
<head>
<meta charset="utf-8">
<title>SkyvoraQ Business Cards</title>
<link href="https://fonts.googleapis.com/css2?family=Exo+2:wght@500;600;800&family=Open+Sans:wght@400;500&display=swap" rel="stylesheet">
<style>
  :root {
    --bg: #e6e6e6;
    --card: #ffffff;
    --navy: #1b2f5c;
    --blue: #1e8fd6;
    --sky: #3fa9e6;
    --text: #2a3550;
    --shadow: rgba(0,0,0,0.18);
  }
  * { box-sizing: border-box; margin: 0; padding: 0; }
  html, body { width: 1200px; height: 852px; overflow: hidden; }
  body {
    background: var(--bg);
    position: relative;
    font-family: "Open Sans", sans-serif;
    color: var(--text);
  }
  .card {
    position: absolute;
    width: 500px;
    height: 286px;
    background: var(--card);
    border-radius: 18px;
    box-shadow: 0 12px 24px var(--shadow);
    overflow: hidden;
  }
  /* Brand side */
  .card--brand { left: 120px; top: 120px; }
  .brand-lockup {
    position: absolute;
    left: 0; right: 0; top: 58px;
    display: flex; flex-direction: column; align-items: center; gap: 14px;
  }
  .brand-dot {
    width: 44px; height: 44px; border-radius: 50%;
    background: var(--blue);
  }
  .brand-name {
    font-family: "Exo 2", sans-serif;
    font-weight: 800;
    font-size: 40px;
    letter-spacing: 7px;
    color: var(--navy);
    text-transform: uppercase;
  }
  .web-row {
    position: absolute; left: 0; right: 0; top: 198px;
    display: flex; align-items: center; justify-content: center; gap: 12px;
    font-size: 12px; letter-spacing: 1px; color: var(--text);
  }
  .web-row .rule { width: 70px; height: 2px; background: var(--sky); }
  .edge-band {
    position: absolute; left: 0; right: 0; bottom: 0; height: 12px;
    display: flex;
  }
  .edge-band .navy { flex: 1; background: var(--navy); }
  .edge-band .blue { flex: 1; background: var(--blue); }

  /* Contact side */
  .card--contact { left: 590px; top: 450px; }
  .decor-circle {
    position: absolute; right: -110px; top: -120px;
    width: 320px; height: 320px; border-radius: 50%;
    background: radial-gradient(circle at 35% 65%, #d7ecfa, #8ec9f0);
    opacity: 0.7;
  }
  .contact-brand {
    position: absolute; left: 32px; top: 104px;
    font-family: "Exo 2", sans-serif; font-weight: 800;
    font-size: 22px; letter-spacing: 4px; color: var(--navy);
    text-transform: uppercase;
  }
  .person { position: absolute; left: 32px; top: 142px; }
  .person-name {
    font-family: "Exo 2", sans-serif; font-weight: 600;
    font-size: 20px; color: var(--blue); line-height: 1.1;
  }
  .person-title { font-size: 11px; color: var(--text); }
  .contact-list {
    position: absolute; left: 32px; top: 188px;
    list-style: none; font-size: 11px; line-height: 15px;
  }
  .contact-list li { display: flex; align-items: center; gap: 8px; }
  .contact-list svg { width: 10px; height: 10px; fill: var(--blue); flex: none; }
  .contact-list .address { padding-left: 18px; }
</style>
</head>
<body>
  <section class="card card--brand" aria-label="Business card, brand side">
    <div class="brand-lockup">
      <span class="brand-dot"></span>
      <span class="brand-name">SkyvoraQ</span>
    </div>
    <div class="web-row">
      <span class="rule"></span>
      <span>www.skyvoraq.com</span>
      <span class="rule"></span>
    </div>
    <div class="edge-band"><span class="navy"></span><span class="blue"></span></div>
  </section>

  <section class="card card--contact" aria-label="Business card, contact side">
    <span class="decor-circle"></span>
    <div class="contact-brand">SkyvoraQ</div>
    <div class="person">
      <div class="person-name">Marcus Delorne</div>
      <div class="person-title">Managing Director</div>
    </div>
    <ul class="contact-list">
      <li><svg viewBox="0 0 10 10"><path d="M2 0h2l1 3-1.5 1a6 6 0 0 0 2.5 2.5L7 5l3 1v2a2 2 0 0 1-2 2A8 8 0 0 1 0 2a2 2 0 0 1 2-2z"/></svg>2045 3318 610</li>
      <li><svg viewBox="0 0 10 10"><rect x="2" y="0" width="6" height="10" rx="1"/></svg>7721 4406 539</li>
      <li><svg viewBox="0 0 10 10"><path d="M0 2h10v6H0z M0 2l5 3 5-3"/></svg>marcus@skyvoraq.com</li>
      <li><svg viewBox="0 0 10 10"><circle cx="5" cy="5" r="5"/></svg>www.skyvoraq.com</li>
      <li class="address">4827 Tollbeck Lane, Marrowick, FL 34951</li>
    </ul>
  </section>
</body>
</html>
```